TORNWICK Pizza Flyer / Menu

Hello so its a new pizza shop called Tornwick. I need a flyer menu designed . it will be 30cm tall and 10.5cm wide. i made one which i have uploaded but as you can see im not very skillfull design wise. I did want the logo on the front with the photo of the counter in the middle and then half the pizza at the bottom. then on the back i wanted all the different toppings ( doesnt have to be the same pics as i have used ) and then drinks and desserts underneath and our contact details. I dont want to include our signature specials. Also facebook/twitter and instagram logos somewhere. the font i have been using is called 'AR CENA' i have attached a rough sketch i have put together to give you an idea too. thanks

Industry/Entity Type

Shop

```html
<!DOCTYPE html>
<html lang="en">
<head>
<meta charset="utf-8">
<title>Tornwick Pizza Menu</title>
<link rel="stylesheet" href="https://fonts.googleapis.com/css2?family=Bubblegum+Sans&family=Roboto+Condensed:wght@700&display=swap">
<style>
  :root {
    --orange: #f7941d;
    --green: #8dc63f;
    --wood: #dcbf95;
    --wood-dark: #c9a878;
    --ring: #f7941d;
    --ink: #1a1a1a;
    --white: #ffffff;
    --board: #e6d1ad;
  }
  * { margin: 0; padding: 0; box-sizing: border-box; }
  html, body { width: 1200px; height: 3429px; overflow: hidden; background: var(--white); }
  .menu { position: relative; width: 1200px; height: 3429px; overflow: hidden; font-family: "Bubblegum Sans", cursive; }
  .abs { position: absolute; }

  .wood-field { left: 0; top: 130px; width: 1200px; height: 1560px;
    background: repeating-linear-gradient(180deg, var(--wood) 0 150px, var(--wood-dark) 150px 154px); }
  .bands { left: 0; top: 0; }

  .header-title { left: 50px; top: 85px; font-size: 46px; color: var(--white); }
  .header-price { right: 78px; top: 65px; font-size: 86px; color: var(--white); }

  .topping { width: 228px; text-align: center; }
  .topping-photo { display: block; margin: 0 auto; width: 146px; height: 146px; border-radius: 50%;
    border: 10px solid var(--ring); background: #eee; }
  .topping-name { margin-top: 32px; font-size: 28px; color: var(--ink); white-space: nowrap; letter-spacing: 0; }

  .section-title { left: 50px; top: 1710px; font-size: 46px; color: var(--white); }

  .photo-tile { width: 206px; height: 172px; }
  .price-board { left: 530px; top: 1870px; width: 636px; height: 754px;
    background: repeating-linear-gradient(180deg, var(--board) 0 120px, #d7bd93 120px 123px); }
  .price-row { left: 560px; width: 578px; display: flex; align-items: baseline; font-size: 32px; color: var(--ink); }
  .price-row::before { content: "•"; width: 64px; }
  .price-row .item { flex: 1; }

  .delivery-line { left: 0; top: 2660px; width: 1200px; text-align: center; font-family: "Roboto Condensed", sans-serif;
    font-weight: 700; font-size: 46px; color: var(--white); }
  .minimum { left: 0; top: 2718px; width: 1200px; text-align: center; font-family: "Roboto Condensed", sans-serif;
    font-weight: 700; font-size: 29px; color: var(--white); }
  .phone { left: 0; top: 2756px; width: 1200px; text-align: center; font-family: "Roboto Condensed", sans-serif;
    font-weight: 700; font-size: 116px; color: var(--white); letter-spacing: 2px; }

  .brand-frame { left: 194px; top: 2949px; width: 915px; height: 297px; border: 11px solid var(--ink);
    border-left: none; border-radius: 0 22px 22px 0; }
  .brand-dot { left: 116px; top: 3045px; width: 170px; height: 170px; border-radius: 50%; background: var(--orange); }
  .brand-tag { left: 70px; top: 2992px; font-size: 28px; color: var(--ink); white-space: nowrap; }
  .brand-name { left: 310px; top: 3030px; font-size: 132px; color: var(--ink); letter-spacing: 3px; line-height: 1; }
  .brand-est { left: 960px; top: 3180px; font-size: 28px; color: var(--ink); }
  .address { left: 0; top: 3262px; width: 1200px; text-align: center; font-size: 31px; color: var(--ink); letter-spacing: 1px; }

  .social-dot { top: 3334px; width: 76px; height: 76px; border-radius: 50%; background: var(--white); }
  .follow { left: 338px; top: 3350px; font-size: 32px; color: var(--white); white-space: nowrap; }
</style>
</head>
<body>
<main class="menu">
  <div class="abs wood-field"></div>

  <svg class="abs bands" width="1200" height="3429" viewBox="0 0 1200 3429">
    <polygon fill="var(--orange)" points="0,0 1200,0 1200,150 1120,165 1060,140 990,160 910,138 850,158 770,142 700,166 620,140 560,160 480,138 400,164 330,142 260,160 190,140 120,162 50,144 0,156"/>
    <polygon fill="var(--green)" points="0,1664 1200,1664 1200,1835 1130,1815 1060,1840 990,1818 930,1838 860,1812 790,1836 720,1814 650,1840 580,1816 510,1838 440,1812 370,1836 300,1816 230,1840 160,1814 90,1836 30,1818 0,1830"/>
    <rect fill="var(--orange)" x="0" y="2651" width="1200" height="300"/>
    <polygon fill="var(--green)" points="0,2925 60,2905 130,2930 200,2908 270,2932 340,2906 410,2930 480,2908 550,2934 620,2906 690,2930 760,2910 830,2934 900,2906 970,2930 1040,2908 1110,2932 1200,2910 1200,3320 0,3320"/>
    <rect fill="var(--orange)" x="0" y="3314" width="1200" height="115"/>
  </svg>

  <div class="abs header-title">BUILD IT!</div>
  <div class="abs header-price">£6.99</div>

  <section class="toppings">
    <div class="abs topping" style="left:23px;top:272px"><div class="topping-photo" role="img" aria-label="Pineapple chunks" style="background:#f2d94e"></div><div class="topping-name">PINEAPPLE</div></div>
    <div class="abs topping" style="left:252px;top:272px"><div class="topping-photo" role="img" aria-label="Pepperoni slices" style="background:#c43a2c"></div><div class="topping-name">PEPPERONI</div></div>
    <div class="abs topping" style="left:485px;top:272px"><div class="topping-photo" role="img" aria-label="Red peppers" style="background:#d9261c"></div><div class="topping-name">RED PEPPER</div></div>
    <div class="abs topping" style="left:713px;top:272px"><div class="topping-photo" role="img" aria-label="Black olives" style="background:#2a2a30"></div><div class="topping-name">BLACK OLIVES</div></div>
    <div class="abs topping" style="left:940px;top:272px"><div class="topping-photo" role="img" aria-label="Spinach leaves" style="background:#3f7a2a"></div><div class="topping-name">SPINACH</div></div>

    <div class="abs topping" style="left:23px;top:507px"><div class="topping-photo" role="img" aria-label="Green olives" style="background:#b7b06b"></div><div class="topping-name">GREEN OLIVES</div></div>
    <div class="abs topping" style="left:252px;top:507px"><div class="topping-photo" role="img" aria-label="Grated mozzarella" style="background:#f4efe2"></div><div class="topping-name">MOZZARELLA</div></div>
    <div class="abs topping" style="left:485px;top:507px"><div class="topping-photo" role="img" aria-label="Green olives" style="background:#5f9a2c"></div><div class="topping-name">GREEN OLIVES</div></div>
    <div class="abs topping" style="left:713px;top:507px"><div class="topping-photo" role="img" aria-label="Ricotta cheese" style="background:#ecebe4"></div><div class="topping-name">RICOTTA</div></div>
    <div class="abs topping" style="left:940px;top:507px"><div class="topping-photo" role="img" aria-label="Green peppers" style="background:#3e9a22"></div><div class="topping-name">GREEN PEPPER</div></div>

    <div class="abs topping" style="left:23px;top:736px"><div class="topping-photo" role="img" aria-label="Diced onion" style="background:#eeeab8"></div><div class="topping-name">ONION</div></div>
    <div class="abs topping" style="left:252px;top:736px"><div class="topping-photo" role="img" aria-label="Grated cheddar" style="background:#f5a623"></div><div class="topping-name">CHEDDAR CHEESE</div></div>
    <div class="abs topping" style="left:485px;top:736px"><div class="topping-photo" role="img" aria-label="Basil leaves" style="background:#59b33d"></div><div class="topping-name">BASIL</div></div>
    <div class="abs topping" style="left:713px;top:736px"><div class="topping-photo" role="img" aria-label="Pulled chicken" style="background:#b97a3a"></div><div class="topping-name">PULLED CHICKEN</div></div>
    <div class="abs topping" style="left:940px;top:736px"><div class="topping-photo" role="img" aria-label="Pulled beef" style="background:#7a3f22"></div><div class="topping-name">PULLED BEEF</div></div>

    <div class="abs topping" style="left:23px;top:964px"><div class="topping-photo" role="img" aria-label="Mushrooms" style="background:#d8ccb8"></div><div class="topping-name">MUSHROOM</div></div>
    <div class="abs topping" style="left:252px;top:964px"><div class="topping-photo" role="img" aria-label="Tomatoes" style="background:#d8311e"></div><div class="topping-name">TOMATO</div></div>
    <div class="abs topping" style="left:485px;top:964px"><div class="topping-photo" role="img" aria-label="Salami slices" style="background:#c73a5c"></div><div class="topping-name">SALAMI</div></div>
    <div class="abs topping" style="left:713px;top:964px"><div class="topping-photo" role="img" aria-label="Capers" style="background:#8c9a3a"></div><div class="topping-name">CAPERS</div></div>
    <div class="abs topping" style="left:940px;top:964px"><div class="topping-photo" role="img" aria-label="Anchovies" style="background:#8a6d45"></div><div class="topping-name">ANCHOVIES</div></div>

    <div class="abs topping" style="left:23px;top:1193px"><div class="topping-photo" role="img" aria-label="Sliced jalapenos" style="background:#2f8a24"></div><div class="topping-name">JALAPENOS</div></div>
    <div class="abs topping" style="left:252px;top:1193px"><div class="topping-photo" role="img" aria-label="Sweetcorn" style="background:#f7c51e"></div><div class="topping-name">CORN</div></div>
    <div class="abs topping" style="left:485px;top:1193px"><div class="topping-photo" role="img" aria-label="Red chillies" style="background:#c81e1e"></div><div class="topping-name">CHILLI</div></div>
    <div class="abs topping" style="left:713px;top:1193px"><div class="topping-photo" role="img" aria-label="Barbecue sauce" style="background:#b08a80"></div><div class="topping-name">B-B-Q</div></div>
    <div class="abs topping" style="left:940px;top:1193px"><div class="topping-photo" role="img" aria-label="Pesto" style="background:#8ccf3a"></div><div class="topping-name">PESTO</div></div>

    <div class="abs topping" style="left:252px;top:1422px"><div class="topping-photo" role="img" aria-label="Chorizo slices" style="background:#c2492e"></div><div class="topping-name">CHORIZO</div></div>
    <div class="abs topping" style="left:485px;top:1422px"><div class="topping-photo" role="img" aria-label="Grated parmesan" style="background:#e8cf6a"></div><div class="topping-name">PARMESAN</div></div>
    <div class="abs topping" style="left:713px;top:1422px"><div class="topping-photo" role="img" aria-label="Sweet chilli sauce" style="background:#e0391f"></div><div class="topping-name">SWEET CHILLI</div></div>
  </section>

  <div class="abs section-title">DRINKS &amp; DESSERTS!</div>

  <section class="dessert-photos">
    <div class="abs photo-tile" role="img" aria-label="Banana and chocolate pizza slices" style="left:57px;top:1870px;background:#8a5a34"></div>
    <div class="abs photo-tile" role="img" aria-label="Chocolate cake" style="left:274px;top:1870px;background:#5a3320"></div>
    <div class="abs photo-tile" role="img" aria-label="Creme brulee" style="left:57px;top:2057px;background:#e7a94a"></div>
    <div class="abs photo-tile" role="img" aria-label="Tiramisu" style="left:274px;top:2057px;background:#c9a27c"></div>
    <div class="abs photo-tile" role="img" aria-label="Blood orange drink" style="left:57px;top:2263px;background:#d8334a"></div>
    <div class="abs photo-tile" role="img" aria-label="Lemonade with lemon" style="left:274px;top:2263px;background:#e8e6a6"></div>
    <div class="abs photo-tile" role="img" aria-label="Glass of orangeade" style="left:57px;top:2452px;background:#f5c21a"></div>
    <div class="abs photo-tile" role="img" aria-label="Can of cola" style="left:274px;top:2452px;background:#c8181e"></div>
  </section>

  <div class="abs price-board"></div>
  <div class="abs price-row" style="top:1935px"><span class="item">BANANA CHOC PIZZA !!!</span><span>3.99</span></div>
  <div class="abs price-row" style="top:2005px"><span class="item">CREME BRULEE</span><span>2.49</span></div>
  <div class="abs price-row" style="top:2076px"><span class="item">TIRAMISU</span><span>2.49</span></div>
  <div class="abs price-row" style="top:2147px"><span class="item">CHOCO DREAM CAKE</span><span>2.49</span></div>
  <div class="abs price-row" style="top:2312px"><span class="item">BLOOD ORANGE</span><span>0.99</span></div>
  <div class="abs price-row" style="top:2383px"><span class="item">ORANGEADE</span><span>0.99</span></div>
  <div class="abs price-row" style="top:2454px"><span class="item">LEMON</span><span>0.99</span></div>
  <div class="abs price-row" style="top:2524px"><span class="item">FIZZ COLA</span><span>0.89</span></div>

  <div class="abs delivery-line">WOOD STONE PIZZA DELIVERY HOT TO YOUR DOOR STEP</div>
  <div class="abs minimum">Minimum Order £12</div>
  <div class="abs phone">0203 555 0178</div>

  <div class="abs brand-frame"></div>
  <div class="abs brand-dot"></div>
  <div class="abs brand-tag">DESIGNER PIZZA</div>
  <div class="abs brand-name">TORNWICK</div>
  <div class="abs brand-est">EST 2016</div>
  <div class="abs address">12 ELM PARADE, HOLLYBANK, SM9 4XQ</div>

  <div class="abs social-dot" style="left:19px"></div>
  <div class="abs social-dot" style="left:122px"></div>
  <div class="abs social-dot" style="left:232px"></div>
  <div class="abs follow">Follow us for updates, offers and if your lucky...a free pizza</div>
</main>
</body>
</html>
```